Design wine label. Brand name The Quillmere

Wine label design for 'The Quillmere'. A few varieties but example-

The Quillmere Shiraz 2016 Bendigo 750ml, 14%alc/vol.

'The quillmere' at top of label, image of sparrow then vintage, variety etc under image.

simple, yet striking and modern look.

Font styles to use
Script

Requirements
Must have
• Image of a sparrow
Nice to have
• Simple image, outline, cartoon or Lino print style. Some colour but not too busy

```html
<!DOCTYPE html>
<html lang="en">
<head>
<meta charset="UTF-8">
<title>The Quillmere – Wine Label</title>
<link rel="stylesheet" href="https://fonts.googleapis.com/css2?family=Josefin+Sans:wght@300;600;700&display=swap">
<style>
  :root {
    --backdrop-light: #e4e2e1;
    --backdrop-dark: #8f8c8b;
    --paper: #efedea;
    --paper-edge: #e2ded9;
    --accent-red: #e0414c;
    --sun-red: #ec5a63;
    --bird-grey: #c9c7c4;
    --fine-print: #b98a8c;
  }
  * { margin: 0; padding: 0; box-sizing: border-box; }
  html, body {
    width: 1200px;
    height: 800px;
    overflow: hidden;
  }
  body {
    background: radial-gradient(circle at 30% 30%, var(--backdrop-light), var(--backdrop-dark));
    font-family: "Josefin Sans", sans-serif;
    position: relative;
  }
  .wine-label {
    position: absolute;
    left: 370px;
    top: 90px;
    width: 460px;
    height: 620px;
    background: var(--paper);
    border-top: 14px solid var(--paper-edge);
    border-bottom: 14px solid var(--paper-edge);
    box-shadow: 0 12px 30px rgba(0,0,0,0.25);
  }
  .emblem {
    position: absolute;
    left: 110px;
    top: 60px;
    width: 240px;
    height: 220px;
  }
  .brand-name {
    position: absolute;
    left: 84px;
    top: 360px;
    font-size: 36px;
    font-weight: 600;
    color: var(--accent-red);
    letter-spacing: 0.5px;
  }
  .wine-style {
    position: absolute;
    left: 122px;
    top: 410px;
    font-size: 22px;
    font-weight: 700;
    color: var(--accent-red);
    letter-spacing: 2px;
  }
  .fine-print {
    position: absolute;
    bottom: 40px;
    font-size: 17px;
    font-weight: 300;
    color: var(--fine-print);
  }
  .volume { left: 34px; }
  .strength { right: 44px; }
</style>
</head>
<body>
  <section class="wine-label">
    <svg class="emblem" viewBox="0 0 240 220" xmlns="http://www.w3.org/2000/svg">
      <circle class="sun" cx="90" cy="95" r="88" fill="var(--sun-red)"/>
      <g role="img" aria-label="Engraved-style illustration of a perched sparrow">
        <ellipse cx="120" cy="110" rx="92" ry="62" fill="var(--bird-grey)" opacity="0.9"/>
      </g>
    </svg>
    <h1 class="brand-name">The Quillmere</h1>
    <p class="wine-style">VINTAGE</p>
    <p class="fine-print volume">750mL</p>
    <p class="fine-print strength">14% alc/vol</p>
  </section>
</body>
</html>
```